Bright Ledger Path's Mortgage Arc

For BrightLedgerPath.org - Creating a sequence of web pages for consumers to understand their mortgage through Mortgage Arc. There are six pages - want the designer to be willing to design and code those six pages. Most of the pages are very similar.

```html
<!DOCTYPE html>
<html lang="en">
<head>
<meta charset="utf-8">
<title>Bright Ledger Path – Member Home</title>
<link rel="stylesheet" href="https://fonts.googleapis.com/css2?family=Poppins:wght@400;500;600;700&display=swap">
<style>
  :root{
    --brand-blue:#1366cc;
    --brand-blue-deep:#1550b4;
    --brand-green:#10c06f;
    --hero-green:#0aa955;
    --hero-blue:#1a4cb0;
    --ink:#2f3a46;
    --card-ink:#414b55;
    --white:#ffffff;
  }
  *{box-sizing:border-box;margin:0;padding:0}
  html,body{width:1200px;height:879px;overflow:hidden}
  body{font-family:"Poppins",sans-serif;background:var(--white);color:var(--ink);position:relative}

  .utility-bar{position:absolute;left:0;top:0;width:1200px;height:54px;background:var(--brand-blue)}
  .utility-btn{position:absolute;top:14px;height:30px;display:flex;align-items:center;justify-content:center;font-size:12px;font-weight:500;color:var(--white);letter-spacing:.2px}
  .utility-btn.logout{left:495px;width:79px;background:var(--brand-green);border:1px solid #5fe0a6}
  .utility-btn.email{left:601px;width:104px;border:1px solid var(--white)}

  .site-header{position:absolute;left:0;top:54px;width:1200px;height:102px;background:var(--white)}
  .brand{position:absolute;left:92px;top:32px;display:flex;align-items:center;gap:12px}
  .brand-mark{width:38px;height:38px;border-radius:6px;background:var(--brand-blue)}
  .brand-name{font-size:24px;font-weight:500;color:var(--brand-blue);letter-spacing:-.2px}
  .main-nav a{position:absolute;top:40px;font-size:15px;color:var(--ink);text-decoration:none;display:flex;align-items:center;gap:8px}
  .caret{width:0;height:0;border-left:4px solid transparent;border-right:4px solid transparent;border-top:5px solid var(--ink);margin-top:3px}

  .hero{position:absolute;left:0;top:156px;width:1200px;height:650px;background:linear-gradient(100deg,var(--hero-green) 0%,#0f8f78 45%,#1760b8 75%,var(--hero-blue) 100%)}
  .hero-title{position:absolute;left:0;width:1200px;top:56px;text-align:center;font-size:40px;font-weight:700;color:var(--white);letter-spacing:-.3px;padding-left:8px}
  .tile{position:absolute;width:184px;height:172px;background:var(--white);border-radius:10px;text-decoration:none}
  .tile-icon{position:absolute;left:59px;top:26px;width:66px;height:66px;border-radius:12px;background:linear-gradient(135deg,#d6f5e7,#d7e4fa)}
  .tile-label{position:absolute;left:0;top:111px;width:184px;text-align:center;font-size:14px;line-height:19.5px;font-weight:500;color:var(--card-ink)}
  .tile-label.single{top:111px}

  .site-footer{position:absolute;left:0;top:806px;width:1200px;height:73px;background:var(--brand-blue);color:var(--white);font-size:13px}
  .copyright{position:absolute;left:94px;top:27px}
  .social{position:absolute;left:546px;top:20px;display:flex;gap:3px}
  .social span{width:33px;height:33px;border-radius:50%;background:#3f86e0}
  .legal{position:absolute;right:93px;top:27px;display:flex;gap:10px}
</style>
</head>
<body>
  <div class="utility-bar">
    <span class="utility-btn logout">LOGOUT</span>
    <span class="utility-btn email">EMAIL DEMOCO</span>
  </div>

  <header class="site-header">
    <div class="brand">
      <span class="brand-mark"></span>
      <span class="brand-name">BrightLedgerPath</span>
    </div>
    <nav class="main-nav">
      <a href="#" style="left:640px">Member Home <span class="caret"></span></a>
      <a href="#" style="left:807px">My Account <span class="caret"></span></a>
      <a href="#" style="left:950px">Blog</a>
      <a href="#" style="left:1038px">Podcast</a>
    </nav>
  </header>

  <main class="hero" role="img" aria-label="Photo of a smiling couple at home, tinted with a green-to-blue brand overlay">
    <h1 class="hero-title">Welcome to Bright Ledger Path</h1>

    <a class="tile" href="#" style="left:211px;top:155px"><span class="tile-icon" role="img" aria-label="Credit report with gauge icon"></span><span class="tile-label">Your 3 TrueRate®<br>Scores / Report</span></a>
    <a class="tile" href="#" style="left:416px;top:155px"><span class="tile-icon" role="img" aria-label="Checklist icon"></span><span class="tile-label">Your Action Plan<br>to Improve Scores</span></a>
    <a class="tile" href="#" style="left:622px;top:155px"><span class="tile-icon" role="img" aria-label="Magnifier over documents icon"></span><span class="tile-label single">Your Score Tracker</span></a>
    <a class="tile" href="#" style="left:828px;top:156px"><span class="tile-icon" role="img" aria-label="Presenter with chart icon"></span><span class="tile-label">Your TrueRate®<br>Score Analyzer</span></a>

    <a class="tile" href="#" style="left:211px;top:349px"><span class="tile-icon" role="img" aria-label="House with document icon"></span><span class="tile-label">Your Home<br>Mortgage</span></a>
    <a class="tile" href="#" style="left:416px;top:349px"><span class="tile-icon" role="img" aria-label="Car with coin icon"></span><span class="tile-label single">Your Auto Loan</span></a>
    <a class="tile" href="#" style="left:622px;top:349px"><span class="tile-icon" role="img" aria-label="Report with charts icon"></span><span class="tile-label">Update Your<br>Report / TrueRate® Scores</span></a>
    <a class="tile" href="#" style="left:828px;top:349px"><span class="tile-icon" role="img" aria-label="Person with settings gear icon"></span><span class="tile-label single">Personal Settings</span></a>
  </main>

  <footer class="site-footer">
    <span class="copyright">Copyright 2023 by Bright Ledger Path</span>
    <div class="social" aria-label="Social links"><span></span><span></span><span></span></div>
    <div class="legal"><span>Terms Of Use</span><span>|</span><span>Privacy Statement</span></div>
  </footer>
</body>
</html>
```